Corvale Homes

To produce a business card design for our newly established house building and development company, We have had a logo design done please see attached, our slogan is "building your home sweet home"
Contact Information for Business Card
Adress on card needs to Read - 58 Elmsworth Lane, Kettering, Northamptonshire NN16 4QT. Director name Dean Vascotti
Requirements
Must have
- Web adress is www.corvale-homes.co.uk
- Email address is info@corvale-homes.co.uk
- phone number 07700 900417

```html
<!DOCTYPE html>
<html lang="en">
<head>
<meta charset="utf-8">
<title>Corvale Homes – Business Card</title>
<link rel="stylesheet" href="https://fonts.googleapis.com/css2?family=Arimo:wght@400;700&display=swap">
<style>
  :root {
    --backdrop: #d9d6d2;
    --charcoal: #3a3a3b;
    --paper: #e7e8e9;
    --lime: #8cc63f;
    --stone: #9a9a9a;
    --white: #ffffff;
    --ink: #2e2e2e;
  }
  * { margin: 0; padding: 0; box-sizing: border-box; }
  html, body {
    width: 900px; height: 1200px; overflow: hidden;
    background: var(--backdrop);
    font-family: "Arimo", Arial, sans-serif;
  }
  .canvas { position: relative; width: 900px; height: 1200px; }

  .card {
    position: absolute; left: 108px; width: 685px; height: 402px;
    overflow: hidden;
  }
  .card--front { top: 175px; background: var(--charcoal); }
  .card--back  { top: 623px; background: var(--paper); }

  /* Front */
  .front-brand {
    position: absolute; left: 0; right: 0; top: 205px;
    text-align: center;
    font-weight: 700; font-size: 54px; letter-spacing: 2px;
    color: var(--lime); line-height: 1;
  }
  .front-slogan {
    position: absolute; left: 0; right: 0; top: 300px;
    text-align: center;
    font-size: 10px; letter-spacing: 5.4px;
    color: var(--white); text-transform: uppercase;
  }

  /* Back */
  .name-tab {
    position: absolute; left: 4px; top: 42px; width: 22px; height: 68px;
    background: var(--lime); border-radius: 0 6px 6px 0;
  }
  .holder-name {
    position: absolute; left: 35px; top: 55px;
    font-weight: 700; font-size: 22px; color: var(--ink);
  }
  .holder-role {
    position: absolute; left: 40px; top: 83px;
    font-size: 16px; color: var(--ink);
  }
  .back-brand {
    position: absolute; right: 48px; top: 90px;
    font-weight: 700; font-size: 30px; color: var(--lime);
  }
  .back-web-top {
    position: absolute; left: 433px; top: 150px;
    font-size: 15px; color: var(--stone);
  }
  .wave { position: absolute; left: 0; top: 0; width: 685px; height: 402px; }

  .contact {
    position: absolute; display: flex; gap: 8px;
    font-size: 18px; line-height: 27px; color: var(--white);
  }
  .contact svg { flex: none; margin-top: 6px; }
  .contact--address { left: 20px; top: 289px; }
  .contact--phone   { left: 372px; top: 289px; }
  .contact--email   { left: 372px; top: 316px; }
  .back-web-bottom {
    position: absolute; left: 0; right: 0; top: 358px;
    text-align: center; font-size: 18px; color: var(--lime);
  }
</style>
</head>
<body>
<main class="canvas">

  <section class="card card--front" aria-label="Card front">
    <div class="front-brand">Corvale Homes</div>
    <div class="front-slogan">Building your home sweet home</div>
  </section>

  <section class="card card--back" aria-label="Card back">
    <svg class="wave" viewBox="0 0 685 402" aria-hidden="true">
      <path fill="var(--lime)" d="M0,232 C90,258 190,270 330,240 S520,170 590,176 C640,181 670,200 685,222 L685,402 L0,402 Z"/>
      <path fill="var(--white)" d="M0,241 C90,267 190,279 330,249 S520,179 590,185 C640,190 670,209 685,231 L685,402 L0,402 Z"/>
      <path fill="var(--charcoal)" d="M0,246 C90,272 190,284 330,254 S520,184 590,190 C640,195 670,214 685,236 L685,402 L0,402 Z"/>
    </svg>

    <div class="name-tab"></div>
    <div class="holder-name">Dean Vascotti</div>
    <div class="holder-role">Director</div>

    <div class="back-brand">Corvale Homes</div>
    <div class="back-web-top">www.corvale-homes.co.uk</div>

    <div class="contact contact--address">
      <svg width="15" height="15" viewBox="0 0 16 16"><circle cx="8" cy="8" r="8" fill="var(--lime)"/><path d="M8 3.5a3 3 0 0 0-3 3c0 2.2 3 6 3 6s3-3.8 3-6a3 3 0 0 0-3-3z" fill="var(--charcoal)"/><circle cx="8" cy="6.5" r="1.1" fill="var(--lime)"/></svg>
      <span>58 Elmsworth Lane, Kettering<br>Northamptonshire NN16 4QT.</span>
    </div>
    <div class="contact contact--phone">
      <svg width="15" height="15" viewBox="0 0 16 16"><circle cx="8" cy="8" r="8" fill="var(--lime)"/><path d="M5.2 4.2l1.4-.3.8 1.9-.9.7c.5 1.1 1.3 1.9 2.4 2.4l.7-.9 1.9.8-.3 1.4c-3.3.2-6.2-2.7-6-6z" fill="var(--charcoal)"/></svg>
      <span>07700 900417</span>
    </div>
    <div class="contact contact--email">
      <svg width="15" height="15" viewBox="0 0 16 16"><circle cx="8" cy="8" r="8" fill="var(--lime)"/><rect x="4" y="5.2" width="8" height="5.6" rx=".6" fill="var(--charcoal)"/><path d="M4.3 5.6L8 8.4l3.7-2.8" stroke="var(--lime)" stroke-width=".8" fill="none"/></svg>
      <span>info@corvale-homes.co.uk</span>
    </div>
    <div class="back-web-bottom">www.corvale-homes.co.uk</div>
  </section>

</main>
</body>
</html>
```